Rings and things/plans. Wedding planning checklist design

We are a wedding videography start-up that's about to launch a chatterly campaign. We need a simple yet premium looking design to showcase a wedding planning checklist which we have written. The main focus of the design should be:

- On A4 pages
- Appeal to young engaged women
- Anyone at home can print it off and stick it onto a fridge
- Premium looking

The contents doesn't have to be on one piece of A4, the list can span more than one page. Also, it doesn't have to be traditional folded brochure style, a full A4 sized list is preferred. The design will potentially be used in further A4 brochure style blog posts. The written checklist and our company logo is attached for reference.

Target Market(s)

Young engaged woman

Industry/Entity Type

Wedding

Requirements
Must have
• Simple and premium feel.
Nice to have
• flexible design that can be reused in the future for blog posts.

```html
<!DOCTYPE html>
<html lang="en">
<head>
<meta charset="utf-8">
<title>The Ultimate Wedding Planning Checklist</title>
<link rel="stylesheet" href="https://fonts.googleapis.com/css2?family=Pinyon+Script&family=Questrial&family=Tinos:ital@0;1&display=swap">
<style>
  :root {
    --paper: #ffffff;
    --ink: #1e1e1e;
    --note: #2a2a2a;
    --brown: #8c5a3a;
    --title-brown: #9a5c38;
    --bullet: #a7b4c3;
    --rule: #3a3a3a;
    --pill: #efe3d6;
    --wood-dark: #6f6a63;
    --wood-mid: #a29c93;
    --wood-light: #c9c4bb;
    --leather: #a8643a;
    --glitter: #c6b79a;
  }
  * { box-sizing: border-box; margin: 0; padding: 0; }
  html, body { width: 1200px; height: 848px; overflow: hidden; background: var(--paper); }
  .page { position: relative; width: 1200px; height: 848px; background: var(--paper); color: var(--ink); }

  .hero {
    position: absolute; left: 27px; top: 27px; width: 1146px; height: 217px;
    background:
      radial-gradient(ellipse 190px 150px at 150px 110px, var(--leather) 0%, rgba(168,100,58,0.6) 45%, transparent 75%),
      radial-gradient(ellipse 150px 140px at 430px 100px, rgba(168,100,58,0.85) 0%, transparent 70%),
      radial-gradient(ellipse 170px 150px at 1010px 120px, var(--glitter) 0%, rgba(198,183,154,0.5) 50%, transparent 80%),
      linear-gradient(180deg, var(--wood-light) 0%, var(--wood-mid) 55%, var(--wood-dark) 100%);
  }
  .hero-title {
    position: absolute; left: 427px; top: 53px; width: 343px; height: 150px;
    background: rgba(240,240,238,0.55);
    border-radius: 10px;
    font-family: "Pinyon Script", cursive; font-weight: 400;
    color: var(--title-brown);
    font-size: 36px; line-height: 40px; text-align: center;
    padding-top: 12px;
  }

  .column { position: absolute; top: 272px; width: 360px; }
  .col-12 { left: 27px; }
  .col-9 { left: 425px; }
  .col-6 { left: 826px; }

  .period {
    display: inline-block; width: 170px; height: 40px; font-weight: 400;
    background: radial-gradient(ellipse at center, var(--pill) 0%, var(--pill) 55%, rgba(239,227,214,0) 100%);
    border-radius: 20px;
    font-family: "Tinos", serif; font-size: 20px; line-height: 40px;
    color: var(--brown); text-align: center; letter-spacing: 0.3px;
  }
  .tasks { list-style: none; margin-top: 18px; }
  .task { position: relative; padding-left: 23px; margin-bottom: 5px; }
  .task::before {
    content: ""; position: absolute; left: 0; top: 2px; width: 11px; height: 11px; background: var(--bullet);
  }
  .task-name { font-family: "Questrial", sans-serif; font-size: 14px; line-height: 15px; }
  .task-note {
    font-family: "Tinos", serif; font-style: italic; font-size: 11px; line-height: 12px;
    color: var(--note); padding-left: 28px;
  }
  .task.blank { margin-top: 34px; height: 14px; margin-bottom: 0; }
  .task.blank + .task.blank { margin-top: 41px; }
  .task.blank::before { top: 0; }
  .task.blank .rule { position: absolute; left: 23px; right: 56px; top: 13px; border-top: 1px solid var(--rule); }

  .signoff { position: absolute; left: 0; width: 1200px; top: 718px; text-align: center; }
  .tagline { font-family: "Tinos", serif; font-style: italic; font-size: 24px; color: var(--ink); line-height: 32px; }
  .brand {
    display: inline-flex; align-items: center; gap: 12px; margin-top: 10px;
  }
  .brand-dot { width: 14px; height: 14px; border-radius: 50%; background: var(--brown); }
  .brand-name {
    font-family: "Questrial", sans-serif; font-size: 34px; color: var(--ink); line-height: 40px;
  }
</style>
</head>
<body>
<div class="page">
  <div class="hero" role="img" aria-label="Photograph of a groom's brown leather brogues and a bride's gold glitter bow sandals on a wooden boardwalk"></div>
  <h1 class="hero-title">The Ultimate<br>Wedding Planning<br>Checklist</h1>

  <section class="column col-12">
    <h2 class="period">12 MONTHS</h2>
    <ul class="tasks">
      <li class="task"><p class="task-name">Decide on a date &amp; venue</p><p class="task-note">The earlier you can reserve these, the better!<br>Will it be a church, garden or beach&nbsp; wedding?</p></li>
      <li class="task"><p class="task-name">Organise a meeting of the parent<br>&amp; determine your budget</p><p class="task-note">Work out how much each family is<br>contributing so that there are no surprises</p></li>
      <li class="task"><p class="task-name">Choose the type of wedding</p><p class="task-note">Form a basic idea of the kind of wedding<br>you would like to have e.g.- simple or lavish?</p></li>
      <li class="task"><p class="task-name">Pick your wedding party</p><p class="task-note">Best man, groomsmen, maid of honor,<br>bridesmaids, flower girl, ring bearer etc.</p></li>
      <li class="task"><p class="task-name">Pick or hire a MC</p><p class="task-note">Someone who enjoys being in the limelight, is confident telling<br>a few jokes, and will make sure everyone is having a good time</p></li>
      <li class="task"><p class="task-name">Start a wedding folder</p><p class="task-note">This is where you can compile your notes<br>and ideas about anything wedding related</p></li>
      <li class="task"><p class="task-name">Hire a planner</p><p class="task-note">A planner will take the stress off you and<br>they can negotiate good deals with vendors</p></li>
      <li class="task"><p class="task-name">Start your guest list</p><p class="task-note">Be realistic about the number of guests to avoid stress later on</p></li>
      <li class="task"><p class="task-name">Research your wedding professionals</p><p class="task-note">These include your videographers, photographers, caterer, DJ,<br>florist, decorator etc. Wedding planners can help with this!</p></li>
      <li class="task"><p class="task-name">Start shopping for wedding rings &amp; your dress</p><p class="task-note">The sooner you buy them, the sooner<br>you can check it off your list</p></li>
    </ul>
  </section>

  <section class="column col-9">
    <h2 class="period">9 MONTHS</h2>
    <ul class="tasks">
      <li class="task"><p class="task-name">Book your official videographers</p><p class="task-note">Velvet &amp; Vow are the way to go!</p></li>
      <li class="task"><p class="task-name">Book your photographer</p><p class="task-note">Consider having an unplugged wedding</p></li>
      <li class="task"><p class="task-name">Book your DJ, florist, caterer,<br>decorator &amp; wedding cake</p><p class="task-note">Use your friends circle! (Friends as vendors)<br>This can be a big cost-cutter</p></li>
      <li class="task"><p class="task-name">Book your celebrant</p><p class="task-note">Have some good conversations with them<br>to determine if they're the right fit</p></li>
      <li class="task blank"><span class="rule"></span></li>
      <li class="task blank"><span class="rule"></span></li>
      <li class="task blank"><span class="rule"></span></li>
    </ul>
  </section>

  <section class="column col-6">
    <h2 class="period">6 MONTHS</h2>
    <ul class="tasks">
      <li class="task"><p class="task-name">Buy wedding party suits/dresses</p><p class="task-note">Your bridal party should complement your gown/suit, but be<br>sure to consider figure types and coloring when selecting outfits</p></li>
      <li class="task"><p class="task-name">Book wedding car</p><p class="task-note">Try and book this as soon as you can to<br>ensure you get the car of your dreams</p></li>
      <li class="task"><p class="task-name">Get your engagement photos done</p><p class="task-note">These can be used for your save-the-date cards. It's also the<br>perfect time to test out your photographer before the big day</p></li>
      <li class="task"><p class="task-name">Launch a website</p><p class="task-note">A good way to broadcast your<br>registry details loud and clear</p></li>
      <li class="task"><p class="task-name">Finalise guest list</p><p class="task-note">Try to avoid any last-minute add-ons.<br>Don't let your parents or in-laws bully you!</p></li>
      <li class="task blank"><span class="rule"></span></li>
      <li class="task blank"><span class="rule"></span></li>
      <li class="task blank"><span class="rule"></span></li>
    </ul>
  </section>

  <footer class="signoff">
    <p class="tagline">Rings and plans!</p>
    <div class="brand">
      <span class="brand-dot"></span>
      <span class="brand-name">Velvet and Vow</span>
    </div>
  </footer>
</div>
</body>
</html>
```